Harbourline Corporate Journeys Capability Statement

Harbourline Corporate Journeys is a Corporate Travel Management company based in Brisbane, Australia. Please review our 'About Us' page of our website to gain an understanding of our company culture (www.harbourlinecorporatejourneys.com.au). We are extremely customer focused. We see ourselves as an extension of our client's business.We require a powerful 1 page infographic that highlights what we do - 'Capability Statement' to use as an initial introduction to prospect clients when they ask for information about us.* Our Core Competencies - Insight / Care / Momentum (this is our tagline so I think the document should follow this format)* A Company snapshot - Office location and website (needs to be editable to add Licence information)* Performance / Key Benefits (needs to editable to add in testimonials and case studies)* Client retention result 96%* Employee retention 98%* Affiliations & Partnerships (we will add)*Awards (see details to include)* Contact Details (at the bottom of the page - Marcus Ellingham marcus@hcjourneys.com.au+61 448 187 226Differentiators (for us to complete so doc must be editable)The format of the document needs to be easily modified when required. I have attached the company logos and branding colours / font etc. Thank youRegardsMiriam

Target Market(s)

Medium businesses Australian based

Industry/Entity Type

Travel Industry

Font styles to use
Sans Serif

Colors
abd036

Requirements
Must have
• Content Outlined and corporate colours. Must be easily editable.

```html
<!DOCTYPE html>
<html lang="en">
<head>
<meta charset="utf-8">
<title>Harbourline Corporate Journeys – Capability Statement</title>
<link href="https://fonts.googleapis.com/css2?family=Oswald:wght@300&family=Poppins:wght@400;500;600;700&display=swap" rel="stylesheet">
<style>
  :root{
    --brand-green:#4db848;
    --brand-lime:#abd036;
    --ink:#2b2b2b;
    --ink-soft:#4a4a4a;
    --dark-band:#2e2e30;
    --card:#ececec;
    --page:#ffffff;
    --backdrop:#efefed;
    --blue:#1f7fc8;
    --cyan:#29b6e8;
  }
  *{box-sizing:border-box;margin:0;padding:0}
  html,body{width:1200px;height:900px;overflow:hidden;background:var(--backdrop)}
  body{font-family:"Poppins",sans-serif;color:var(--ink)}
  .statement{position:absolute;left:292px;top:10px;width:616px;height:880px;background:var(--page);
    box-shadow:0 2px 10px rgba(0,0,0,.12);overflow:hidden}

  .hero{position:absolute;left:9px;top:13px;width:598px;height:280px;
    background:linear-gradient(180deg,#dcd9e2 0%,#c3bcc4 40%,#8c7466 66%,#3a2c25 84%,#1f1916 100%)}
  .hero-rule{position:absolute;left:9px;top:290px;width:598px;height:4px;background:var(--brand-green)}
  .hero-title{position:absolute;left:0;right:0;top:242px;text-align:center;color:#fff;font-weight:700;
    font-size:17.5px;line-height:24px;letter-spacing:.2px;text-shadow:0 1px 3px rgba(0,0,0,.6)}

  .brand-panel{position:absolute;left:9px;top:13px;width:250px;height:80px}
  .brand-panel svg{position:absolute;inset:0}
  .brand-name{position:absolute;left:30px;top:14px;width:200px;font-size:16px;line-height:18px;
    font-weight:500;color:var(--ink-soft)}
  .brand-tagline{position:absolute;left:66px;top:54px;font-size:7px;font-weight:600;color:var(--brand-green);letter-spacing:.3px}

  .about-title{position:absolute;left:0;right:0;top:312px;text-align:center;font-family:"Oswald",sans-serif;
    font-weight:300;font-size:54px;line-height:64px;color:var(--ink)}
  .about-lead{position:absolute;left:60px;right:60px;top:386px;text-align:center;font-size:10.4px;
    line-height:15px;font-weight:600;color:var(--ink)}
  .about-body{position:absolute;left:66px;right:66px;top:418px;text-align:justify;text-align-last:center;
    font-size:10.2px;line-height:14.6px;color:var(--ink-soft)}

  .competency{position:absolute;width:100px;text-align:center;font-size:13px;color:var(--ink-soft)}
  .competency svg{display:block;margin:0 auto 4px;width:44px;height:44px;fill:none;stroke:var(--brand-green);stroke-width:1.6;stroke-linecap:round;stroke-linejoin:round}

  .stats-card{position:absolute;left:346px;top:510px;width:238px;height:294px;background:var(--card);
    border-radius:16px;box-shadow:2px 3px 6px rgba(0,0,0,.18)}
  .stat{position:absolute;left:60px;width:112px;height:112px}
  .stat svg{position:absolute;inset:0}
  .stat-figure{position:absolute;left:0;right:0;top:30px;text-align:center;font-size:18px;font-weight:700;color:#16508f}
  .stat-label{position:absolute;left:0;right:0;top:55px;text-align:center;font-size:8px;line-height:12px;font-weight:600;color:var(--ink)}

  .footer svg{position:absolute;left:0;top:815px}
  .footer-phone{position:absolute;left:32px;top:829px;color:#fff;font-size:14px;font-weight:600}
  .footer-phone svg{position:static;vertical-align:-2px;margin-right:3px}
  .footer-contact{position:absolute;right:40px;top:846px;color:#fff;font-size:11px;font-weight:600}
</style>
</head>
<body>
<main class="statement">
  <div class="hero" role="img" aria-label="Photo of an airliner at the gate seen through a departure lounge window at sunset"></div>
  <div class="hero-rule"></div>
  <h2 class="hero-title">OUR CORE COMPETENCIES<br>INSIGHT / CARE / MOMENTUM</h2>

  <div class="brand-panel">
    <svg width="250" height="80" viewBox="0 0 250 80">
      <defs><linearGradient id="panelFill" x1="0" y1="0" x2="0" y2="1"><stop offset="0" stop-color="#ffffff"/><stop offset="1" stop-color="#d9d9d9"/></linearGradient></defs>
      <path d="M0 0 H245 L232 70 Q230 76 222 76 H0 Z" fill="url(#panelFill)" opacity=".95"/>
      <path d="M245 0 L232 70 Q230 76 222 76 H0" fill="none" stroke="var(--brand-green)" stroke-width="3"/>
    </svg>
    <div class="brand-name">Harbourline Corporate Journeys</div>
    <div class="brand-tagline">INSIGHT | CARE | MOMENTUM</div>
  </div>

  <h1 class="about-title">ABOUT US</h1>
  <p class="about-lead">Harbourline Corporate Journeys was founded on the vision of delivering<br>a superior customer experience and end to end business travel management solutions.</p>
  <p class="about-body">Opening for business in 2005, HCJ is a progressive business travel management company and corporate travel specialist. We focus on engaging industry-best consultants and market leading technology, including Waypoint Nexus, to provide a tailored, complete, personalised business travel offering.</p>

  <div class="competency" style="left:51px;top:524px">
    <svg viewBox="0 0 44 44"><circle cx="22" cy="22" r="16" stroke-dasharray="3 3"/><circle cx="22" cy="22" r="4"/><circle cx="22" cy="7" r="2.5"/><circle cx="8" cy="29" r="2.5"/><circle cx="36" cy="29" r="2.5"/><path d="M22 10v8M11 28l8-4M33 28l-8-4"/></svg>Process</div>
  <div class="competency" style="left:167px;top:524px">
    <svg viewBox="0 0 44 44"><circle cx="20" cy="22" r="15"/><path d="M28 9a15 15 0 0 1 0 26"/><path d="M24 16c-1-2-7-2-7 1.5s7 2 7 5.5-6 3.5-7 1M20.5 13v18"/></svg>Savings</div>
  <div class="competency" style="left:51px;top:622px">
    <svg viewBox="0 0 44 44"><path d="M8 4h20l6 6v30H8z"/><path d="M13 12h10M13 17h15M13 22h15M13 27h12M13 32h10"/><circle cx="33" cy="31" r="6" fill="#fff"/><path d="M30 31l2 2 4-4"/></svg>Control</div>
  <div class="competency" style="left:167px;top:622px">
    <svg viewBox="0 0 44 44"><rect x="4" y="6" width="30" height="22" rx="1"/><path d="M15 28v6M11 34h12"/><rect x="28" y="16" width="12" height="22" rx="1.5" fill="#fff"/><path d="M32 35h4"/></svg>Mobile</div>
  <div class="competency" style="left:51px;top:716px">
    <svg viewBox="0 0 44 44"><path d="M12 4h20v34H12z"/><path d="M8 8h4M8 8v34h20v-4"/><circle cx="17" cy="11" r="3"/><path d="M22 11h6M16 18h12M16 23h12M16 28h12M16 33h8"/></svg>Policy</div>
  <div class="competency" style="left:167px;top:716px">
    <svg viewBox="0 0 44 44"><path d="M6 4v34h34"/><path d="M11 32l7-9 6 5 6-10 7 4"/><circle cx="18" cy="23" r="1.8"/><circle cx="24" cy="28" r="1.8"/><circle cx="30" cy="18" r="1.8"/><path d="M10 8h6M10 12h4"/></svg>Visibility</div>

  <section class="stats-card">
    <div class="stat" style="top:15px">
      <svg viewBox="0 0 112 112">
        <defs><linearGradient id="blueRing" x1="0" y1="0" x2="0" y2="1"><stop offset="0" stop-color="var(--blue)"/><stop offset="1" stop-color="var(--cyan)"/></linearGradient></defs>
        <circle cx="56" cy="56" r="50" fill="none" stroke="#cfcfcf" stroke-width="4"/>
        <circle cx="56" cy="56" r="50" fill="none" stroke="url(#blueRing)" stroke-width="4" stroke-dasharray="270 314" transform="rotate(-90 56 56)"/>
      </svg>
      <div class="stat-figure">98%</div>
      <div class="stat-label">EMPLOYEE<br>RETENTION</div>
    </div>
    <div class="stat" style="top:153px">
      <svg viewBox="0 0 112 112">
        <defs><linearGradient id="warmRing" x1="0" y1="0" x2="0" y2="1"><stop offset="0" stop-color="#d9263a"/><stop offset=".6" stop-color="#ef6a2c"/><stop offset="1" stop-color="#f2b52a"/></linearGradient></defs>
        <circle cx="56" cy="56" r="50" fill="none" stroke="#cfcfcf" stroke-width="4"/>
        <circle cx="56" cy="56" r="50" fill="none" stroke="url(#warmRing)" stroke-width="4" stroke-dasharray="262 314" transform="rotate(-90 56 56)"/>
      </svg>
      <div class="stat-figure">96%</div>
      <div class="stat-label">CLIENT<br>RETENTION<br>RESULT</div>
    </div>
  </section>

  <footer class="footer">
    <svg width="616" height="65" viewBox="0 0 616 65">
      <path d="M206 23 H616 V55 H214 Z" fill="var(--dark-band)"/>
      <path d="M0 5 H198 L214 55 H0 Z" fill="var(--brand-green)"/>
    </svg>
    <div class="footer-phone"><svg width="12" height="12" viewBox="0 0 24 24"><path d="M6.6 10.8a15 15 0 0 0 6.6 6.6l2.2-2.2a1 1 0 0 1 1-.25 11 11 0 0 0 3.6.6 1 1 0 0 1 1 1V20a1 1 0 0 1-1 1A17 17 0 0 1 3 4a1 1 0 0 1 1-1h3.5a1 1 0 0 1 1 1c0 1.25.2 2.45.6 3.6a1 1 0 0 1-.25 1z" fill="#fff"/></svg>+61 452 639 814</div>
    <div class="footer-contact">Marcus Ellingham marcus@hcjourneys.com.au</div>
  </footer>
</main>
</body>
</html>
```